Business Cards for Lean-In-Wise

I need a business card that uses elements of my color pallet and book along with my company name and logo. The primary thing I'd like to have stand out is the word Lean-In-Wise (i'd like to see this word in the orange from my pallet)
On the back of the card I want it to say Stop being Accountable, Be Lean-In-Wise

Contact Information for Business Card

Summit Hearthgroup logo, Lean-In-Wise, email - rtm@summithearthgroup.example, phone 555-208-4917, Portland | Halifax

Requirements
Nice to have
• colors from my color pallet

```html
<!DOCTYPE html>
<html lang="en">
<head>
<meta charset="utf-8">
<title>Lean-In-Wise Business Cards</title>
<link rel="stylesheet" href="https://fonts.googleapis.com/css2?family=Oswald:wght@500;600&family=Montserrat:wght@400;500;600&display=swap">
<style>
  :root {
    --backdrop: #2b2b2d;
    --navy-deep: #1d1f5c;
    --navy: #273a8c;
    --paper: #f1f1f1;
    --orange: #e2561f;
    --logo-blue: #2a8fd0;
    --white: #ffffff;
  }
  * { margin: 0; padding: 0; box-sizing: border-box; }
  html, body { width: 1200px; height: 800px; overflow: hidden; }
  body {
    background: var(--backdrop);
    position: relative;
    font-family: "Montserrat", sans-serif;
  }
  .card {
    position: absolute;
    width: 560px;
    height: 320px;
    overflow: hidden;
    box-shadow: 0 10px 24px rgba(0,0,0,.45);
    background: linear-gradient(100deg, var(--navy-deep), var(--navy));
  }
  .card--front { left: 360px; top: 40px; }
  .card--back { left: 300px; top: 420px; }

  .front__band {
    height: 96px;
    background: var(--paper);
    display: flex;
    align-items: center;
    justify-content: space-between;
    padding: 0 28px 0 30px;
  }
  .front__headline {
    font-family: "Oswald", sans-serif;
    font-weight: 600;
    font-size: 62px;
    letter-spacing: 1px;
    color: var(--orange);
    line-height: 1;
  }
  .partner-name {
    font-family: "Montserrat", sans-serif;
    font-weight: 600;
    font-size: 15px;
    color: var(--navy);
  }
  .front__body {
    display: flex;
    justify-content: space-between;
    padding: 24px 22px 0 24px;
  }
  .brand {
    width: 190px;
    display: flex;
    flex-direction: column;
    align-items: center;
    text-align: center;
    padding-top: 4px;
  }
  .brand__dot {
    width: 60px; height: 60px;
    border-radius: 50%;
    background: var(--logo-blue);
    margin-bottom: 14px;
  }
  .brand__name {
    font-weight: 500;
    font-size: 21px;
    line-height: 1.15;
    color: var(--logo-blue);
  }
  .brand__tagline {
    margin-top: 8px;
    font-size: 9px;
    color: var(--logo-blue);
    font-style: italic;
  }
  .contact { padding-top: 20px; color: var(--white); width: 300px; }
  .contact__name { font-weight: 600; font-size: 24px; letter-spacing: 1px; margin-bottom: 12px; }
  .contact__list { list-style: none; }
  .contact__item {
    display: flex; align-items: center; gap: 10px;
    font-size: 13.5px; line-height: 1.7;
    white-space: nowrap;
  }
  .contact__item svg { width: 14px; height: 14px; flex: none; }

  .back__slogan {
    position: absolute;
    left: 44px; top: 58px;
    font-family: "Oswald", sans-serif;
    font-weight: 600;
    font-size: 62px;
    line-height: 1.08;
    color: var(--white);
    text-transform: uppercase;
    white-space: nowrap;
  }
  .back__slogan .accent { color: var(--orange); font-size: 76px; }
</style>
</head>
<body>

  <section class="card card--front">
    <div class="front__band">
      <h1 class="front__headline">LEAN-IN-WISE</h1>
      <span class="partner-name">Crestline 90</span>
    </div>
    <div class="front__body">
      <div class="brand">
        <span class="brand__dot"></span>
        <span class="brand__name">Summit<br>Hearthgroup</span>
        <span class="brand__tagline">Together We Climb Higher!</span>
      </div>
      <div class="contact">
        <p class="contact__name">Dana Whitlock</p>
        <ul class="contact__list">
          <li class="contact__item">
            <svg viewBox="0 0 16 16"><path fill="#e2561f" d="M8 1 1 7h2v8h4v-5h2v5h4V7h2z"/></svg>
            Portland | Halifax
          </li>
          <li class="contact__item">
            <svg viewBox="0 0 16 16"><path fill="#e2561f" d="M4 1l2.5 3-1.5 2a8 8 0 0 0 5 5l2-1.5 3 2.5-1.5 2.5C8 15 1 8 1.5 3z"/></svg>
            555-208-4917
          </li>
          <li class="contact__item">
            <svg viewBox="0 0 16 16"><rect x="1" y="3" width="14" height="10" fill="#e2561f"/><path d="M1 3l7 6 7-6" fill="none" stroke="#273a8c" stroke-width="1.4"/></svg>
            rtm@summithearthgroup.example
          </li>
          <li class="contact__item">
            <svg viewBox="0 0 16 16"><g fill="none" stroke="#e2561f" stroke-width="1.3"><circle cx="8" cy="8" r="6.5"/><ellipse cx="8" cy="8" rx="3" ry="6.5"/><path d="M1.5 8h13M2.5 4.5h11M2.5 11.5h11"/></g></svg>
            www.summithearthgroup.example
          </li>
        </ul>
      </div>
    </div>
  </section>

  <section class="card card--back">
    <p class="back__slogan">Stop being<br>Accountable<br>Be <span class="accent">Lean-In-Wise</span></p>
  </section>

</body>
</html>
```